Jahreskalender 2019 / Wandkalender für Foto- und Videoagentur
Immer wieder gern.
Zielgruppe
Wir sind eine Foto und Videoagentur für Nachrichtenthemen in Deutschland. Unser Wandkalender ist für Kunden und Einsatzkräfte.
Aufgabenstellung
Der Wandkalender 2019 soll im Format DIN A1 (84 x 59,4 cm) gedruckt werden. Sie bekommen von uns Fotos und diese müssen gut bearbeitet in den Wandkalender eingefügt werden. Ein Kameramann muss ausgeschnitten werden und etwas dominant im Kalender vorkommen. Sie bekommen zur Ansicht die alten Kalender. Es sollten alle wichtigen Feiertrage im Kalender vorkommen. Auch die Info Box wie in den anderen Kalender muss wieder eingefügt werden.

```html
<!DOCTYPE html>
<html lang="de">
<head>
<meta charset="utf-8">
<title>Jahreskalender 2019 – Lagebild</title>
<link href="https://fonts.googleapis.com/css2?family=Montserrat:wght@900&family=Oswald:wght@500;700&family=Roboto:wght@400;700&display=swap" rel="stylesheet">
<style>
:root{
  --bg:#000;
  --ink:#111;
  --white:#fff;
  --weekend:#e4e8b6;
  --holiday:#fcdcae;
  --holiday-ink:#d0281e;
  --note-ink:#8a1a12;
  --line:#9a9a8a;
  --lime:#b3cb3c;
  --rh:18.6px;
}
*{box-sizing:border-box;margin:0;padding:0}
html,body{width:1200px;height:848px;overflow:hidden;background:var(--bg)}
.poster{position:relative;width:1200px;height:848px;overflow:hidden;background:var(--bg);font-family:"Roboto",Arial,sans-serif}

/* photo areas */
.photo{position:absolute}
.photo-forest{left:960px;top:330px;width:240px;height:330px;background:linear-gradient(180deg,#0b0b0b 0%,#2d2f2b 30%,#3f4236 60%,#2a2520 100%)}
.photo-fire{left:720px;top:640px;width:480px;height:208px;background:radial-gradient(ellipse at 35% 30%,#f8b248 0%,#e06a1c 30%,#6d2a0e 65%,#1a0c06 100%)}
.photo-accident{left:0;top:640px;width:420px;height:208px;background:linear-gradient(160deg,#1c2230 0%,#3a3630 40%,#9a5f3a 70%,#5a3a28 100%)}
.photo-rescue{left:410px;top:648px;width:328px;height:220px;background:var(--white);transform:rotate(-2deg);padding:8px 8px 0}
.photo-rescue div{width:100%;height:100%;background:linear-gradient(180deg,#b9cfe0 0%,#8fae9a 35%,#c2352c 60%,#4a3d3a 100%)}
.photo-cameraman{left:1010px;top:480px;width:190px;height:368px;background:linear-gradient(180deg,rgba(40,36,34,0) 0%,#3a3330 18%,#2a2624 40%,#b9d12c 62%,#8fa622 100%)}

/* calendar */
.calendar{position:absolute;left:17px;top:39px;width:951px}
.months{display:grid;grid-template-columns:repeat(12,1fr);height:32px;background:#0c0a0a}
.months h2{font-family:"Oswald",sans-serif;font-weight:700;font-size:16px;color:var(--white);text-align:center;line-height:32px;letter-spacing:.2px}
.grid{display:grid;grid-template-columns:repeat(12,1fr);margin-top:5px;background:var(--white);border-left:1px solid var(--line)}
.month{list-style:none;border-right:1px solid var(--line);
  background:linear-gradient(180deg,var(--weekend) 0,var(--weekend) calc(var(--rh)*2),var(--white) calc(var(--rh)*2),var(--white) calc(var(--rh)*7));
  background-size:100% calc(var(--rh)*7);
  background-position:0 calc(var(--s)*var(--rh))}
.month li{position:relative;height:var(--rh);border-bottom:1px solid var(--line);display:flex;align-items:center}
.month li b{display:block;width:25px;height:100%;border-right:1px solid var(--line);font-size:6.6px;font-weight:700;color:var(--ink);line-height:calc(var(--rh) - 1px);padding-left:1px;white-space:nowrap}
.month li.blank{background:var(--white)}
.month li.hol{background:var(--holiday)}
.month li.hol b{color:var(--holiday-ink)}
.month li span{position:absolute;left:27px;bottom:1px;font-size:5.4px;line-height:1.15;color:var(--note-ink);font-weight:700;white-space:nowrap}
.month li em{position:absolute;right:1px;top:0;font-style:normal;font-size:5px;color:var(--ink)}

/* right column */
.year{position:absolute;left:982px;top:14px;width:200px;text-align:center;font-family:"Montserrat",sans-serif;font-weight:900;font-size:78px;line-height:1;color:var(--white);letter-spacing:-2px}
.brand{position:absolute;left:979px;top:96px;width:204px;height:56px;text-align:center;font-family:"Roboto",sans-serif;font-weight:700;font-size:40px;line-height:56px;color:var(--white)}
.info{position:absolute;left:979px;top:171px;width:204px;height:163px;background:var(--lime);border:3px solid var(--white);color:var(--white);text-align:center;font-family:"Oswald",sans-serif;font-weight:700;padding-top:7px}
.info p{line-height:1.12}
.info .q{font-size:12.5px}
.info .sub{font-size:12px;font-weight:500;font-style:italic;margin-bottom:12px}
.info .call{font-size:12.5px}
.info .num{font-size:14px;letter-spacing:.5px}
.info .small{font-size:5px;font-weight:500;margin-bottom:6px}
.info .web{font-size:18px;font-style:italic;margin-top:3px}
</style>
</head>
<body>
<main class="poster">
  <div class="photo photo-forest" role="img" aria-label="Kiefernwald mit dichtem Brandrauch"></div>
  <div class="photo photo-fire" role="img" aria-label="Feuerwehrleute vor einem lichterloh brennenden Gebäude"></div>
  <div class="photo photo-accident" role="img" aria-label="Nächtlicher Lkw-Unfall auf der Autobahn mit Feuerwehrfahrzeugen, Luftaufnahme"></div>
  <div class="photo photo-rescue" role="img" aria-label="Wasserretter versorgen eine gerettete Person im Boot auf einem Fluss"><div></div></div>
  <div class="photo photo-cameraman" role="img" aria-label="Freigestellter Kameramann in Warnweste mit Videokamera"></div>

  <section class="calendar">
    <header class="months">
      <h2>JANUAR</h2><h2>FEBRUAR</h2><h2>MÄRZ</h2><h2>APRIL</h2><h2>MAI</h2><h2>JUNI</h2><h2>JULI</h2><h2>AUGUST</h2><h2>SEPTEMBER</h2><h2>OKTOBER</h2><h2>NOVEMBER</h2><h2>DEZEMBER</h2>
    </header>
    <div class="grid">
      <ul class="month" style="--s:4">
        <li class="hol"><b>1 Di</b><span>Neujahr</span></li><li><b>2 Mi</b></li><li><b>3 Do</b></li><li><b>4 Fr</b></li><li><b>5 Sa</b></li><li class="hol"><b>6 So</b><span>Heilige 3 Könige</span></li><li><b>7 Mo</b><em>02</em></li><li><b>8 Di</b></li><li><b>9 Mi</b></li><li><b>10 Do</b></li><li><b>11 Fr</b></li><li><b>12 Sa</b></li><li><b>13 So</b></li><li><b>14 Mo</b><em>03</em></li><li><b>15 Di</b></li><li><b>16 Mi</b></li><li><b>17 Do</b></li><li><b>18 Fr</b></li><li><b>19 Sa</b></li><li><b>20 So</b></li><li><b>21 Mo</b><em>04</em></li><li><b>22 Di</b></li><li><b>23 Mi</b></li><li><b>24 Do</b></li><li><b>25 Fr</b></li><li><b>26 Sa</b></li><li><b>27 So</b></li><li><b>28 Mo</b><em>05</em></li><li><b>29 Di</b></li><li><b>30 Mi</b></li><li><b>31 Do</b></li>
      </ul>
      <ul class="month" style="--s:1">
        <li><b>1 Fr</b></li><li><b>2 Sa</b></li><li><b>3 So</b></li><li><b>4 Mo</b><em>06</em></li><li><b>5 Di</b></li><li><b>6 Mi</b></li><li><b>7 Do</b></li><li><b>8 Fr</b></li><li><b>9 Sa</b></li><li><b>10 So</b></li><li><b>11 Mo</b><em>07</em></li><li><b>12 Di</b></li><li><b>13 Mi</b></li><li><b>14 Do</b></li><li><b>15 Fr</b></li><li><b>16 Sa</b></li><li><b>17 So</b></li><li><b>18 Mo</b><em>08</em></li><li><b>19 Di</b></li><li><b>20 Mi</b></li><li><b>21 Do</b></li><li><b>22 Fr</b></li><li><b>23 Sa</b></li><li><b>24 So</b></li><li><b>25 Mo</b><em>09</em></li><li><b>26 Di</b></li><li><b>27 Mi</b></li><li><b>28 Do</b></li><li class="blank"><b></b></li><li class="blank"><b></b></li><li class="blank"><b></b></li>
      </ul>
      <ul class="month" style="--s:1">
        <li><b>1 Fr</b></li><li><b>2 Sa</b></li><li><b>3 So</b></li><li><b>4 Mo</b><em>10</em></li><li><b>5 Di</b></li><li><b>6 Mi</b></li><li><b>7 Do</b></li><li><b>8 Fr</b></li><li><b>9 Sa</b></li><li><b>10 So</b></li><li><b>11 Mo</b><em>11</em></li><li><b>12 Di</b></li><li><b>13 Mi</b></li><li><b>14 Do</b></li><li><b>15 Fr</b></li><li><b>16 Sa</b></li><li><b>17 So</b></li><li><b>18 Mo</b><em>12</em></li><li><b>19 Di</b></li><li><b>20 Mi</b></li><li><b>21 Do</b></li><li><b>22 Fr</b></li><li><b>23 Sa</b></li><li><b>24 So</b></li><li><b>25 Mo</b><em>13</em></li><li><b>26 Di</b></li><li><b>27 Mi</b></li><li><b>28 Do</b></li><li><b>29 Fr</b></li><li><b>30 Sa</b></li><li><b>31 So</b></li>
      </ul>
      <ul class="month" style="--s:5">
        <li><b>1 Mo</b><em>14</em></li><li><b>2 Di</b></li><li><b>3 Mi</b></li><li><b>4 Do</b></li><li><b>5 Fr</b></li><li><b>6 Sa</b></li><li><b>7 So</b></li><li><b>8 Mo</b><em>15</em></li><li><b>9 Di</b></li><li><b>10 Mi</b></li><li><b>11 Do</b></li><li><b>12 Fr</b></li><li><b>13 Sa</b></li><li><b>14 So</b></li><li><b>15 Mo</b><em>16</em></li><li><b>16 Di</b></li><li><b>17 Mi</b></li><li><b>18 Do</b></li><li class="hol"><b>19 Fr</b><span>Karfreitag</span></li><li><b>20 Sa</b></li><li><b>21 So</b></li><li class="hol"><b>22 Mo</b><span>Ostermontag</span><em>17</em></li><li><b>23 Di</b></li><li><b>24 Mi</b></li><li><b>25 Do</b></li><li><b>26 Fr</b></li><li><b>27 Sa</b></li><li><b>28 So</b></li><li><b>29 Mo</b><em>18</em></li><li><b>30 Di</b></li><li class="blank"><b></b></li>
      </ul>
      <ul class="month" style="--s:3">
        <li class="hol"><b>1 Mi</b><span>Tag der Arbeit</span></li><li><b>2 Do</b></li><li><b>3 Fr</b></li><li><b>4 Sa</b></li><li><b>5 So</b></li><li><b>6 Mo</b><em>19</em></li><li><b>7 Di</b></li><li><b>8 Mi</b></li><li><b>9 Do</b></li><li><b>10 Fr</b></li><li><b>11 Sa</b></li><li><b>12 So</b></li><li><b>13 Mo</b><em>20</em></li><li><b>14 Di</b></li><li><b>15 Mi</b></li><li><b>16 Do</b></li><li><b>17 Fr</b></li><li><b>18 Sa</b></li><li><b>19 So</b></li><li><b>20 Mo</b><em>21</em></li><li><b>21 Di</b></li><li><b>22 Mi</b></li><li><b>23 Do</b></li><li><b>24 Fr</b></li><li><b>25 Sa</b></li><li><b>26 So</b></li><li><b>27 Mo</b><em>22</em></li><li><b>28 Di</b></li><li><b>29 Mi</b></li><li class="hol"><b>30 Do</b><span>Christi<br>Himmelfahrt</span></li><li><b>31 Fr</b></li>
      </ul>
      <ul class="month" style="--s:0">
        <li><b>1 Sa</b></li><li><b>2 So</b></li><li><b>3 Mo</b><em>23</em></li><li><b>4 Di</b></li><li><b>5 Mi</b></li><li><b>6 Do</b></li><li><b>7 Fr</b></li><li><b>8 Sa</b></li><li><b>9 So</b></li><li class="hol"><b>10 Mo</b><span>Pfingstmontag</span><em>24</em></li><li><b>11 Di</b></li><li><b>12 Mi</b></li><li><b>13 Do</b></li><li><b>14 Fr</b></li><li><b>15 Sa</b></li><li><b>16 So</b></li><li><b>17 Mo</b><em>25</em></li><li><b>18 Di</b></li><li><b>19 Mi</b></li><li class="hol"><b>20 Do</b><span>Fronleichnam</span></li><li><b>21 Fr</b></li><li><b>22 Sa</b></li><li><b>23 So</b></li><li><b>24 Mo</b><em>26</em></li><li><b>25 Di</b></li><li><b>26 Mi</b></li><li><b>27 Do</b></li><li><b>28 Fr</b></li><li><b>29 Sa</b></li><li><b>30 So</b></li><li class="blank"><b></b></li>
      </ul>
      <ul class="month" style="--s:5">
        <li><b>1 Mo</b><em>27</em></li><li><b>2 Di</b></li><li><b>3 Mi</b></li><li><b>4 Do</b></li><li><b>5 Fr</b></li><li><b>6 Sa</b></li><li><b>7 So</b></li><li><b>8 Mo</b><em>28</em></li><li><b>9 Di</b></li><li><b>10 Mi</b></li><li><b>11 Do</b></li><li><b>12 Fr</b></li><li><b>13 Sa</b></li><li><b>14 So</b></li><li><b>15 Mo</b><em>29</em></li><li><b>16 Di</b></li><li><b>17 Mi</b></li><li><b>18 Do</b></li><li><b>19 Fr</b></li><li><b>20 Sa</b></li><li><b>21 So</b></li><li><b>22 Mo</b><em>30</em></li><li><b>23 Di</b></li><li><b>24 Mi</b></li><li><b>25 Do</b></li><li><b>26 Fr</b></li><li><b>27 Sa</b></li><li><b>28 So</b></li><li><b>29 Mo</b><em>31</em></li><li><b>30 Di</b></li><li><b>31 Mi</b></li>
      </ul>
      <ul class="month" style="--s:2">
        <li><b>1 Do</b></li><li><b>2 Fr</b></li><li><b>3 Sa</b></li><li><b>4 So</b></li><li><b>5 Mo</b><em>32</em></li><li><b>6 Di</b></li><li><b>7 Mi</b></li><li><b>8 Do</b></li><li><b>9 Fr</b></li><li><b>10 Sa</b></li><li><b>11 So</b></li><li><b>12 Mo</b><em>33</em></li><li><b>13 Di</b></li><li><b>14 Mi</b></li><li class="hol"><b>15 Do</b><span>Mariä<br>Himmelfahrt</span></li><li><b>16 Fr</b></li><li><b>17 Sa</b></li><li><b>18 So</b></li><li><b>19 Mo</b><em>34</em></li><li><b>20 Di</b></li><li><b>21 Mi</b></li><li><b>22 Do</b></li><li><b>23 Fr</b></li><li><b>24 Sa</b></li><li><b>25 So</b></li><li><b>26 Mo</b><em>35</em></li><li><b>27 Di</b></li><li><b>28 Mi</b></li><li><b>29 Do</b></li><li><b>30 Fr</b></li><li><b>31 Sa</b></li>
      </ul>
      <ul class="month" style="--s:6">
        <li><b>1 So</b></li><li><b>2 Mo</b><em>36</em></li><li><b>3 Di</b></li><li><b>4 Mi</b></li><li><b>5 Do</b></li><li><b>6 Fr</b></li><li><b>7 Sa</b></li><li><b>8 So</b></li><li><b>9 Mo</b><em>37</em></li><li><b>10 Di</b></li><li><b>11 Mi</b></li><li><b>12 Do</b></li><li><b>13 Fr</b></li><li><b>14 Sa</b></li><li><b>15 So</b></li><li><b>16 Mo</b><em>38</em></li><li><b>17 Di</b></li><li><b>18 Mi</b></li><li><b>19 Do</b></li><li><b>20 Fr</b></li><li><b>21 Sa</b></li><li><b>22 So</b></li><li><b>23 Mo</b><em>39</em></li><li><b>24 Di</b></li><li><b>25 Mi</b></li><li><b>26 Do</b></li><li><b>27 Fr</b></li><li><b>28 Sa</b></li><li><b>29 So</b></li><li><b>30 Mo</b><em>40</em></li><li class="blank"><b></b></li>
      </ul>
      <ul class="month" style="--s:4">
        <li><b>1 Di</b></li><li><b>2 Mi</b></li><li class="hol"><b>3 Do</b><span>Tag der Dt.<br>Einheit</span></li><li><b>4 Fr</b></li><li><b>5 Sa</b></li><li><b>6 So</b></li><li><b>7 Mo</b><em>41</em></li><li><b>8 Di</b></li><li><b>9 Mi</b></li><li><b>10 Do</b></li><li><b>11 Fr</b></li><li><b>12 Sa</b></li><li><b>13 So</b></li><li><b>14 Mo</b><em>42</em></li><li><b>15 Di</b></li><li><b>16 Mi</b></li><li><b>17 Do</b></li><li><b>18 Fr</b></li><li><b>19 Sa</b></li><li><b>20 So</b></li><li><b>21 Mo</b><em>43</em></li><li><b>22 Di</b></li><li><b>23 Mi</b></li><li><b>24 Do</b></li><li><b>25 Fr</b></li><li><b>26 Sa</b></li><li><b>27 So</b></li><li><b>28 Mo</b><em>44</em></li><li><b>29 Di</b></li><li><b>30 Mi</b></li><li class="hol"><b>31 Do</b><span>Reformationstag</span></li>
      </ul>
      <ul class="month" style="--s:1">
        <li class="hol"><b>1 Fr</b><span>Allerheiligen</span></li><li><b>2 Sa</b></li><li><b>3 So</b></li><li><b>4 Mo</b><em>45</em></li><li><b>5 Di</b></li><li><b>6 Mi</b></li><li><b>7 Do</b></li><li><b>8 Fr</b></li><li><b>9 Sa</b></li><li><b>10 So</b></li><li><b>11 Mo</b><em>46</em></li><li><b>12 Di</b></li><li><b>13 Mi</b></li><li><b>14 Do</b></li><li><b>15 Fr</b></li><li><b>16 Sa</b></li><li><b>17 So</b></li><li><b>18 Mo</b><em>47</em></li><li><b>19 Di</b></li><li class="hol"><b>20 Mi</b><span>Buß- und Bettag</span></li><li><b>21 Do</b></li><li><b>22 Fr</b></li><li><b>23 Sa</b></li><li><b>24 So</b></li><li><b>25 Mo</b><em>48</em></li><li><b>26 Di</b></li><li><b>27 Mi</b></li><li><b>28 Do</b></li><li><b>29 Fr</b></li><li><b>30 Sa</b></li><li class="blank"><b></b></li>
      </ul>
      <ul class="month" style="--s:6">
        <li><b>1 So</b></li><li><b>2 Mo</b><em>49</em></li><li><b>3 Di</b></li><li><b>4 Mi</b></li><li><b>5 Do</b></li><li><b>6 Fr</b></li><li><b>7 Sa</b></li><li><b>8 So</b></li><li><b>9 Mo</b><em>50</em></li><li><b>10 Di</b></li><li><b>11 Mi</b></li><li><b>12 Do</b></li><li><b>13 Fr</b></li><li><b>14 Sa</b></li><li><b>15 So</b></li><li><b>16 Mo</b><em>51</em></li><li><b>17 Di</b></li><li><b>18 Mi</b></li><li><b>19 Do</b></li><li><b>20 Fr</b></li><li><b>21 Sa</b></li><li><b>22 So</b></li><li><b>23 Mo</b><em>52</em></li><li><b>24 Di</b></li><li class="hol"><b>25 Mi</b><span>Weihnachten</span></li><li class="hol"><b>26 Do</b><span>Weihnachten</span></li><li><b>27 Fr</b></li><li><b>28 Sa</b></li><li><b>29 So</b></li><li><b>30 Mo</b><em>01</em></li><li><b>31 Di</b></li>
      </ul>
    </div>
  </section>

  <div class="year">2019</div>
  <div class="brand">Lagebild</div>
  <aside class="info">
    <p class="q">Kenntnis von aktuellen Ereignissen?</p>
    <p class="sub">Unfälle, Brände oder Polizeieinsätze.</p>
    <p class="call">Rufen Sie uns an! 24h-Telefon</p>
    <p class="num">0800/55 12 309</p>
    <p class="small">(Aus dem dt. Festnetz und Mobil kostenlos)</p>
    <p class="call">Oder schreiben Sie uns eine SMS</p>
    <p class="num">0171/48 62 517</p>
    <p class="web">www.lagebild.de</p>
  </aside>
</main>
</body>
</html>
```